Business Cards and Stationary for Physio
Brookvale Phsyiotherapy Clinic
Business Cards and Stationary for Physio -
Creative Brief
Simple
First Last
Physiotherapist B. Physio
Street Name, City, Zip
info@brookvalephysiotherapy.example
www.brookvalephysiotherapy.example
Brookvale Phsyiotherapy Clinic. Next Appointment Date Time

```html
<!DOCTYPE html>
<html lang="en">
<head>
<meta charset="utf-8">
<title>Brookvale Phsyiotherapy Clinic – Business Card and Appointment Card</title>
<link rel="stylesheet" href="https://fonts.googleapis.com/css2?family=Open+Sans:wght@400;600;700&display=swap">
<style>
  :root {
    --green: #8dc63f;
    --navy: #2b3990;
    --ink: #4a4a4a;
    --muted: #6d6d6d;
    --card: #ffffff;
    --backdrop: #e9e7e4;
    --rule: #9a9a9a;
  }
  * { box-sizing: border-box; margin: 0; padding: 0; }
  html, body {
    width: 1200px; height: 857px; overflow: hidden;
    background: var(--backdrop);
    font-family: "Open Sans", Arial, sans-serif;
  }
  .canvas { position: relative; width: 1200px; height: 857px; }

  .card {
    position: absolute;
    background: var(--card);
    border-radius: 22px;
    overflow: hidden;
    box-shadow: 0 6px 18px rgba(0,0,0,0.18);
  }

  /* Front: business card */
  .card-front { left: 168px; top: 132px; width: 545px; height: 300px; }
  .card-front .edge-band {
    position: absolute; left: 0; top: 0; bottom: 0; width: 22px;
    background: var(--green);
  }
  .brand {
    position: absolute; top: 36px; right: 40px;
    display: flex; align-items: center; gap: 8px;
    color: var(--navy); font-weight: 700; font-size: 17px; line-height: 1.05;
  }
  .brand .mark { width: 14px; height: 14px; border-radius: 50%; background: var(--green); flex: none; }
  .brand-name small { display: block; font-size: 10px; letter-spacing: 0.4px; }
  .person {
    position: absolute; left: 310px; top: 136px; width: 180px;
    text-align: center;
  }
  .person-name { color: var(--green); font-weight: 700; font-size: 26px; line-height: 1; }
  .person-title { color: var(--green); font-weight: 600; font-size: 10px; margin-top: 5px; }
  .contact {
    position: absolute; left: 246px; top: 206px;
    font-size: 11.5px; line-height: 17px; color: var(--muted);
    list-style: none;
  }
  .contact .label { color: var(--navy); }

  /* Back: appointment card */
  .card-back { left: 456px; top: 451px; width: 540px; height: 307px; }
  .appt-header {
    height: 56px; background: var(--green);
    color: var(--navy); font-size: 23px; font-weight: 400;
    display: flex; align-items: center; justify-content: center;
  }
  .appt-fields {
    position: absolute; left: 40px; top: 194px;
    display: flex; gap: 30px; font-size: 13px; color: var(--ink);
  }
  .appt-field { display: flex; align-items: flex-end; gap: 6px; }
  .appt-field .line { display: inline-block; width: 175px; border-bottom: 1px dashed var(--rule); height: 12px; }
  .weekdays {
    position: absolute; left: 40px; top: 238px;
    display: flex; gap: 14px; list-style: none;
    font-size: 14px; font-weight: 600; color: var(--ink);
  }
  .weekdays li { display: flex; flex-direction: column; align-items: center; gap: 4px; width: 32px; }
  .weekdays .box { width: 13px; height: 13px; border: 1.5px solid var(--ink); }
  .card-back .brand { top: auto; bottom: 28px; right: 30px; font-size: 14px; }
  .card-back .brand-name small { font-size: 8px; }
</style>
</head>
<body>
<main class="canvas">
  <section class="card card-front" aria-label="Business card front">
    <div class="edge-band"></div>
    <div class="brand">
      <span class="mark"></span>
      <span class="brand-name">Brookvale<small>PHSYIOTHERAPY CLINIC</small></span>
    </div>
    <div class="person">
      <p class="person-name">First Last</p>
      <p class="person-title">Physiotherapist B. Physio</p>
    </div>
    <ul class="contact">
      <li><span class="label">Phone:</span> 555-014-2270</li>
      <li><span class="label">Address:</span> Street Name, City, Zip</li>
      <li><span class="label">Email:</span> info@brookvalephysiotherapy.example</li>
      <li><span class="label">Web address:</span> www.brookvalephysiotherapy.example</li>
    </ul>
  </section>

  <section class="card card-back" aria-label="Appointment card">
    <header class="appt-header">Next Appointment</header>
    <div class="appt-fields">
      <span class="appt-field">Date : <span class="line"></span></span>
      <span class="appt-field">Time : <span class="line"></span></span>
    </div>
    <ul class="weekdays">
      <li>Mon<span class="box"></span></li>
      <li>Tue<span class="box"></span></li>
      <li>Wed<span class="box"></span></li>
      <li>Thu<span class="box"></span></li>
      <li>Fri<span class="box"></span></li>
    </ul>
    <div class="brand">
      <span class="mark"></span>
      <span class="brand-name">Brookvale<small>PHSYIOTHERAPY CLINIC</small></span>
    </div>
  </section>
</main>
</body>
</html>
```